Redesign Colorful Business Card

Please redesign the card attached. It is too busy. Please don't eliminate any of the words. The repetivite word "free" can be used less often.

Target Market(s)

College Students.

Contact Information for Business Card

The details listed in the attached image

Font styles to use
Sans Serif

Requirements
Must have
• A clear and simple presentation and must be attractive.

```html
<!DOCTYPE html>
<html lang="en">
<head>
<meta charset="utf-8">
<title>StudyNimbl Business Card</title>
<link rel="stylesheet" href="https://fonts.googleapis.com/css2?family=Exo+2:wght@600&family=Roboto:wght@700&display=swap">
<style>
  :root {
    --page: #e4e5e7;
    --blue-light: #2f9ad8;
    --blue-mid: #2383c6;
    --blue-deep: #17599c;
    --band-cyan: #6ccbee;
    --band-pale: #c4e8f8;
    --orange: #f7a21b;
    --burst-top: #ffb21e;
    --burst-bottom: #ee3a24;
    --white: #ffffff;
  }
  html, body {
    margin: 0;
    width: 1200px;
    height: 840px;
    overflow: hidden;
    background: var(--page);
  }
  .canvas {
    position: relative;
    width: 1200px;
    height: 840px;
  }
  .card {
    position: absolute;
    left: 317px;
    width: 590px;
    height: 331px;
    display: block;
    overflow: hidden;
  }
  .card--front { top: 58px; }
  .card--back { top: 432px; }

  .band-cyan { fill: var(--band-cyan); }
  .band-pale { fill: var(--band-pale); }
  .zone-deep { fill: var(--blue-deep); }
  .zone-mid { fill: var(--blue-mid); }
  .rule { stroke: var(--white); stroke-width: 2.5; }

  .brand-name {
    font-family: "Exo 2", sans-serif;
    font-weight: 600;
    fill: var(--white);
  }
  .brand-dot { fill: var(--band-cyan); }
  .web-address {
    font-family: "Exo 2", sans-serif;
    font-weight: 600;
    font-size: 13px;
    fill: var(--white);
    letter-spacing: 0.3px;
  }
  .copyright {
    font-family: "Roboto", sans-serif;
    font-weight: 700;
    font-size: 6.4px;
    fill: var(--white);
  }

  .benefit-box {
    fill: none;
    stroke: var(--orange);
    stroke-width: 3.5;
  }
  .check-ring {
    fill: none;
    stroke: var(--orange);
    stroke-width: 3.5;
  }
  .check-mark {
    fill: none;
    stroke: var(--white);
    stroke-width: 3.2;
    stroke-linecap: round;
    stroke-linejoin: round;
  }
  .benefit-text {
    font-family: "Roboto", sans-serif;
    font-weight: 700;
    font-size: 9.2px;
    fill: var(--white);
    text-anchor: middle;
  }
  .burst {
    stroke: var(--white);
    stroke-width: 4;
    stroke-linejoin: round;
  }
  .burst-label {
    font-family: "Roboto", sans-serif;
    font-weight: 700;
    font-size: 22px;
    fill: var(--white);
    text-anchor: middle;
  }
</style>
</head>
<body>
<main class="canvas">

  <!-- Front of card -->
  <svg class="card card--front" viewBox="0 0 492 276" role="img" aria-label="Front of the StudyNimbl business card">
    <defs>
      <linearGradient id="front-fill" x1="0" y1="0" x2="1" y2="1">
        <stop offset="0" stop-color="var(--blue-light)"/>
        <stop offset="1" stop-color="var(--blue-deep)"/>
      </linearGradient>
    </defs>
    <rect class="card-base" width="492" height="276" fill="url(#front-fill)"/>
    <path class="band-cyan" d="M215,276 C330,230 430,130 470,0 L492,0 L492,25 C460,140 380,230 300,276 Z"/>
    <path class="band-pale" d="M300,276 C380,230 460,140 492,25 L492,75 C470,160 420,230 360,276 Z"/>
    <path class="zone-deep" d="M360,276 C420,230 470,160 492,75 L492,276 Z"/>

    <g class="brand">
      <circle class="brand-dot" cx="100" cy="127" r="9"/>
      <text class="brand-name" x="116" y="138" font-size="30">StudyNimbl</text>
    </g>
    <text class="web-address" x="156" y="225" text-anchor="middle">StudyNimbl.com</text>

    <g class="copyright">
      <text x="484" y="259" text-anchor="end">Copyright Nimbl Services</text>
      <text x="484" y="268" text-anchor="end">LLC 2013-2022 All Right Reserved</text>
    </g>
  </svg>

  <!-- Back of card -->
  <svg class="card card--back" viewBox="0 0 492 276" role="img" aria-label="Back of the StudyNimbl business card">
    <defs>
      <linearGradient id="back-fill" x1="0" y1="0" x2="1" y2="1">
        <stop offset="0" stop-color="var(--blue-mid)"/>
        <stop offset="1" stop-color="var(--blue-deep)"/>
      </linearGradient>
      <linearGradient id="corner-fill" x1="0" y1="0" x2="1" y2="1">
        <stop offset="0" stop-color="#43b9ec"/>
        <stop offset="1" stop-color="var(--blue-mid)"/>
      </linearGradient>
      <linearGradient id="burst-fill" x1="0" y1="0" x2="0" y2="1">
        <stop offset="0" stop-color="var(--burst-top)"/>
        <stop offset="1" stop-color="var(--burst-bottom)"/>
      </linearGradient>
    </defs>
    <rect class="card-base" width="492" height="276" fill="url(#back-fill)"/>

    <path class="corner-glow" fill="url(#corner-fill)" d="M0,0 L200,0 C150,90 80,160 0,178 Z"/>
    <path class="band-cyan" d="M200,0 L232,0 C180,100 90,175 0,190 L0,178 C80,160 150,90 200,0 Z"/>
    <path class="band-pale" d="M232,0 L245,0 C192,108 98,185 0,198 L0,190 C90,175 180,100 232,0 Z"/>

    <path class="band-pale" d="M285,276 C350,190 425,150 492,148 L492,160 C430,165 360,200 300,276 Z"/>
    <path class="band-cyan" d="M300,276 C360,200 430,165 492,160 L492,172 C430,178 370,215 318,276 Z"/>
    <path class="zone-mid" d="M318,276 C370,215 430,178 492,172 L492,276 Z"/>

    <line class="rule" x1="205" y1="6" x2="492" y2="6"/>
    <line class="rule" x1="0" y1="267" x2="315" y2="267"/>

    <text class="brand-name" x="76" y="76" font-size="15" text-anchor="middle">StudyNimbl</text>

    <g class="benefit">
      <circle class="check-ring" cx="266" cy="60" r="17"/>
      <path class="check-mark" d="M258,60 L264,67 L275,52"/>
      <rect class="benefit-box" x="301" y="28" width="123" height="64" rx="5"/>
      <text class="benefit-text" x="362.5" y="57">MEMORIZE</text>
      <text class="benefit-text" x="362.5" y="69">ANYTHING QUICKLY</text>
    </g>

    <g class="benefit">
      <circle class="check-ring" cx="197" cy="135" r="17"/>
      <path class="check-mark" d="M189,135 L195,142 L206,127"/>
      <rect class="benefit-box" x="230" y="103" width="124" height="65" rx="5"/>
      <text class="benefit-text" x="292" y="132">CUT STUDY TIME</text>
      <text class="benefit-text" x="292" y="144">DOWN BY UPTO 50%</text>
    </g>

    <g class="benefit">
      <circle class="check-ring" cx="126" cy="212" r="17"/>
      <path class="check-mark" d="M118,212 L124,219 L135,204"/>
      <rect class="benefit-box" x="158" y="180" width="126" height="65" rx="5"/>
      <text class="benefit-text" x="221" y="203">LEARN A SUBJECT</text>
      <text class="benefit-text" x="221" y="215">WITHOUT HAVING TO</text>
      <text class="benefit-text" x="221" y="227">GO TO CLASS</text>
    </g>

    <g class="offer">
      <polygon class="burst" fill="url(#burst-fill)" points="469,210 454.5,221.7 461.2,239 442.8,241.8 440,260.2 422.7,253.5 411,268 399.3,253.5 382,260.2 379.2,241.8 360.8,239 367.5,221.7 353,210 367.5,198.3 360.8,181 379.2,178.2 382,159.8 399.3,166.5 411,152 422.7,166.5 440,159.8 442.8,178.2 461.2,181 454.5,198.3"/>
      <text class="burst-label" x="411" y="218" transform="rotate(-18 411 210)">FREE</text>
    </g>
  </svg>

</main>
</body>
</html>
```